A professional business to business web site for a contract agency called VONTAREX.

We need a very clean, very professional web site created for business to business. It is an informational web site with 3 pages. We are a company that offers contract employee placements into primarily the pharmaceutical industry. I have attached a file that describes the company more fully.

Hi,

I'm sorry if I wasn't clear, but I need to have the HTML pages created so I can just upload the files you give me to the web hosting site.

Please let me know if you have any questions.

Thanks for working on my project!

Hello,

I didn't put this in the description, but I would need the web site set up on the web hosting site as well.  The web hosting site is abrightkettle.  I want a copy of all the files as well.

Thanks,
Miles

Reason: I'm sorry, unexpectedly, I have been very busy and I haven't been able to devote the time necessary for this. I am extending the deadline by 10 days. Thank you for your patience. Thanks.

Reason: Hi everyone, I apologize again, but everything has been so busy here that I haven't been able to give this attention. I plan to work on this over the next few days. Thanks and sorry again, Miles.

Reason: I'm sorry this is taking longer than planned. I have been extremely busy. I have increased the budget on this project. Thanks.

Target Market(s)

Large professional corporations mainly in the pharmaceutical industry. The audience is hiring decisions makers within the companies and potential job candidates/job seekers.

Industry/Entity Type

Pharmaceutical

Font styles to use
Sans Serif

Requirements
Must have
• Must have a clean look that mimics the pharmaceutical industry web sites. VERY professional.
Nice to have
• A nice picture of professional business/pharma/technical people looking like a team. Colors are listed on the attached Word document.
Should not have
• No animation. Not too busy.

```html
<!DOCTYPE html>
<html lang="en">
<head>
<meta charset="utf-8">
<title>VONTAREX – Contract Placements</title>
<link href="https://fonts.googleapis.com/css2?family=Roboto+Condensed:wght@300;400&family=PT+Sans:wght@400;700&family=Short+Stack&display=swap" rel="stylesheet">
<style>
:root{
  --navy:#1a2f86;
  --navy-dark:#13206a;
  --blue:#3f6fc2;
  --sky:#3aa6ec;
  --ink:#333;
  --heading:#1f3a5c;
  --icon:#2b5479;
  --band:#f3f3f3;
  --footer:#2c2c2c;
  --rule:#c9c9c9;
}
*{margin:0;padding:0;box-sizing:border-box}
html,body{width:1200px;height:1132px;overflow:hidden;background:#fff}
body{font-family:Arial,Helvetica,sans-serif;color:var(--ink);position:relative}
.brand{position:absolute;left:128px;top:40px;display:flex;align-items:center;gap:10px;font-family:"PT Sans",sans-serif;font-size:24px;letter-spacing:5px;color:var(--navy)}
.brand .dot{width:26px;height:26px;border-radius:50%;background:var(--navy)}
.contact{position:absolute;top:9px;right:98px;display:flex;gap:34px;font-size:14px;color:#444}
.contact span{display:flex;align-items:center;gap:8px}
.contact .phone{color:#4a4a1a}
.follow{position:absolute;top:62px;right:100px;display:flex;align-items:center;gap:6px;font-size:12px;font-weight:bold;color:#111}
.follow .label{margin-right:4px}
.follow i{width:29px;height:29px;border-radius:50%;display:block}
.nav{position:absolute;left:118px;top:111px;width:953px;height:46px;border-radius:6px;background:linear-gradient(#2f4fb0,var(--navy-dark));display:flex;align-items:center;padding-left:0}
.nav a{color:#fff;text-decoration:none;font-family:"PT Sans",sans-serif;font-size:14px;height:36px;line-height:36px;padding:0 29px;border-right:1px solid #2a5fd0}
.nav a:last-child{border-right:0}
.slider{position:absolute;left:122px;top:174px;width:950px;height:325px;border-radius:4px;overflow:hidden;background:linear-gradient(#3f74c8,#2a4ea8);box-shadow:4px 3px 3px rgba(0,0,0,.15)}
.slider .photo{position:absolute;left:430px;top:0;width:520px;height:325px;background:linear-gradient(100deg,#eef0f2 0%,#dfe4ea 40%,#c8b79a 80%,#b08a5a 100%)}
.slider svg{position:absolute;left:380px;top:0}
.slide-copy{position:absolute;left:24px;top:30px;font-family:"Short Stack",cursive;color:#fff}
.slide-copy h2{font-weight:400;font-size:29px;margin-bottom:14px}
.slide-copy li{list-style:none;font-size:15px;height:30px;display:flex;align-items:center;gap:9px}
.slide-copy li svg{position:static}
.find{position:absolute;left:22px;top:266px;width:125px;height:33px;border-radius:7px;border:1px solid #ccc;background:linear-gradient(#555,#111);color:#fff;font-family:"Short Stack",cursive;font-size:15px;display:flex;align-items:center;justify-content:center;gap:8px}
.find b{width:16px;height:14px;background:#eee;border-radius:2px;position:relative}
.find b:after{content:"";position:absolute;left:5px;top:3px;border-left:7px solid #222;border-top:4px solid transparent;border-bottom:4px solid transparent}
.dots{position:absolute;top:508px;left:595px;display:flex;gap:8px}
.dots i{width:13px;height:13px;border-radius:50%;background:#999;border:2px solid #ddd}
.dots i.on{background:var(--navy-dark)}
.welcome{position:absolute;top:538px;left:0;width:1200px;display:flex;justify-content:center;align-items:center;gap:14px;font-family:"Roboto Condensed",sans-serif;font-size:31px;color:var(--navy-dark)}
.welcome .brand-inline{font-family:"PT Sans",sans-serif;font-size:21px;letter-spacing:5px;color:var(--navy);display:flex;align-items:center;gap:8px}
.welcome .brand-inline i{width:22px;height:22px;border-radius:50%;background:var(--navy)}
.rule{position:absolute;top:584px;left:405px;width:436px;border-top:1px solid var(--rule)}
.intro{position:absolute;top:592px;left:122px;width:960px;text-align:center;font-size:12px;line-height:18px;color:#444}
.intro strong{color:#333}
.intro p+p{margin-top:18px}
.intro .more{display:block;font-weight:bold;color:#1d47a0}
.band{position:absolute;top:773px;left:0;width:1200px;height:245px;background:var(--band)}
.feature{position:absolute;top:797px;width:280px}
.feature h3{display:flex;align-items:center;gap:11px;font-size:26px;color:var(--heading);height:50px}
.feature h3 i{width:50px;height:50px;border-radius:50%;background:var(--icon);display:flex;align-items:center;justify-content:center}
.feature hr{border:0;border-top:1px solid var(--rule);margin:14px 0 14px;width:274px}
.feature p{font-size:12px;line-height:19px;color:#555;text-align:justify}
.btn{position:absolute;top:166px;right:0;width:127px;height:35px;border-radius:3px;background:linear-gradient(#24476f,#0e2239);color:#fff;font-family:"PT Sans",sans-serif;font-size:14px;font-weight:bold;display:flex;align-items:center}
.btn span{flex:1;text-align:center}
.btn b{width:26px;height:100%;border-left:1px solid #456;display:flex;align-items:center;justify-content:center;font-size:18px;background:#1b3656;border-radius:0 3px 3px 0}
.footer{position:absolute;top:1047px;left:0;width:1200px;height:85px;background:var(--footer)}
.footer .brand{top:48px;left:128px;color:#bbb;font-size:16px}
.footer .brand .dot{width:20px;height:20px;background:#bbb}
.footer .social{position:absolute;left:411px;top:31px;display:flex;gap:12px}
.footer .social i{width:28px;height:28px;border-radius:5px;background:linear-gradient(#fff,#bbb);display:block}
.footer nav{position:absolute;right:100px;top:28px;font-size:12px;color:#fff;text-align:right;line-height:18px}
.footer nav a{color:#fff;text-decoration:none}
.footer nav .sep{margin:0 10px}
</style>
</head>
<body>
<header>
  <div class="brand" style="top:48px"><span class="dot"></span>VONTAREX</div>
  <div class="contact">
    <span><svg width="32" height="18" viewBox="0 0 32 18"><path d="M0 3h8M2 7h6M4 11h4" stroke="#333" stroke-width="1.5"/><rect x="11" y="1" width="20" height="15" fill="none" stroke="#333" stroke-width="1.6"/><path d="M11 1l10 8 10-8" fill="none" stroke="#333" stroke-width="1.6"/></svg>hello@vontarex-mail.com</span>
    <span class="phone"><svg width="16" height="22" viewBox="0 0 16 22"><rect x="2" y="1" width="11" height="20" rx="2" fill="none" stroke="#2d3a8a" stroke-width="1.8"/><rect x="4" y="4" width="7" height="10" fill="#2d3a8a"/></svg>555-214-0387</span>
  </div>
  <div class="follow"><span class="label">FOLLOW US ON:</span><i style="background:#4bb3e8"></i><i style="background:#ee6a20"></i><i style="background:#2c4b9a"></i><i style="background:#c8c8c8"></i></div>
</header>

<nav class="nav">
  <a href="#">Home</a><a href="#">About Us</a><a href="#">Energy</a><a href="#">What we do</a><a href="#">News</a><a href="#">Contact Us</a>
</nav>

<section class="slider">
  <div class="photo" role="img" aria-label="Photo of a smiling team of pharmaceutical and medical professionals in white coats"></div>
  <svg width="120" height="325" viewBox="0 0 120 325">
    <path d="M0 0H48C20 110 28 230 70 325H0Z" fill="#2f5bb5"/>
    <path d="M48 0H70C42 110 48 230 88 325H66C28 230 20 110 48 0Z" fill="#0d1f78"/>
    <path d="M70 0H82C54 110 60 230 100 325H88C48 230 42 110 70 0Z" fill="#fff"/>
    <path d="M82 0H102C72 110 80 230 114 325H100C60 230 54 110 82 0Z" fill="#3aa6ec"/>
  </svg>
  <div class="slide-copy">
    <h2>For the pharmaceutical</h2>
    <ul>
      <li><svg width="16" height="16" viewBox="0 0 16 16"><rect x="1" y="3" width="12" height="12" fill="none" stroke="#fff" stroke-width="1.6"/><path d="M4 8l3 3 8-10" fill="none" stroke="#fff" stroke-width="2"/></svg>Lpsum is simply dummy</li>
      <li><svg width="16" height="16" viewBox="0 0 16 16"><rect x="1" y="3" width="12" height="12" fill="none" stroke="#fff" stroke-width="1.6"/><path d="M4 8l3 3 8-10" fill="none" stroke="#fff" stroke-width="2"/></svg>Text of the printing and typesetting</li>
      <li><svg width="16" height="16" viewBox="0 0 16 16"><rect x="1" y="3" width="12" height="12" fill="none" stroke="#fff" stroke-width="1.6"/><path d="M4 8l3 3 8-10" fill="none" stroke="#fff" stroke-width="2"/></svg>Industry. Lorem Ipsum has been</li>
      <li><svg width="16" height="16" viewBox="0 0 16 16"><rect x="1" y="3" width="12" height="12" fill="none" stroke="#fff" stroke-width="1.6"/><path d="M4 8l3 3 8-10" fill="none" stroke="#fff" stroke-width="2"/></svg>The industry's standard dummy</li>
      <li><svg width="16" height="16" viewBox="0 0 16 16"><rect x="1" y="3" width="12" height="12" fill="none" stroke="#fff" stroke-width="1.6"/><path d="M4 8l3 3 8-10" fill="none" stroke="#fff" stroke-width="2"/></svg>Text ever since the 1500s,</li>
    </ul>
  </div>
  <div class="find">Find More <b></b></div>
</section>
<div class="dots"><i class="on"></i><i></i><i></i></div>

<h1 class="welcome" style="font-weight:400">Welcome to <span class="brand-inline"><i></i>VONTAREX</span></h1>
<div class="rule"></div>
<div class="intro">
  <p><strong>Vestibulum rutrum pharetra diam, eget dapibus leo vehicula ut. Fusce aliquam, odio eget adipiscing lobortis.Vestibulum rutrum pharetra diam, eget dapibus leo vehicula ut. Fusce aliquam, odio eget adipiscing lobortis.Vestibulum rutrum pharetra diam,</strong> eget dapibus leo vehicula ut. Fusce aliquam, odio eget adipiscing lobortis.Vestibulum rutrum pharetra diam, eget dapibus leo vehicula ut. Fusce aliquam, odio eget adipiscing lobortis.Vestibulum rutrum pharetra diam, eget dapibus leo vehicula ut. Fusce aliquam, odio eget adipiscing lobortis.Vestibulum rutrum pharetra diam, eget dapibus leo vehicula ut. Fusce aliquam, odio eget adipiscing lobortis.Vestibulum rutrum pharetra diam, eget dapibus leo vehicula ut. Fusce aliquam, odio eget adipiscing lobortis.</p>
  <p>Vestibulum rutrum pharetra diam, eget dapibus leo vehicula ut. Fusce aliquam, odio eget adipiscing lobortis.Vestibulum rutrum pharetra diam, eget dapibus leo vehicula ut. Fusce aliquam, odio eget adipiscing lobortis.<a class="more">More [+]</a></p>
</div>

<section class="band">
  <article class="feature" style="left:151px;top:24px">
    <h3><i><svg width="26" height="30" viewBox="0 0 26 30"><circle cx="10" cy="3" r="2" fill="#fff"/><circle cx="16" cy="5" r="1.5" fill="#fff"/><path d="M9 9h8v6l6 12H3l6-12z" fill="#fff"/></svg></i>Lorem Ipsum</h3>
    <hr>
    <p>Lorem Ipsum is simply dummy text of the printing and typesetting industry. Lorem Ipsum has been the industry's standard dummy text ever since the Ipsum has been the industry's...</p>
    <div class="btn"><span>Read More</span><b>+</b></div>
  </article>
  <article class="feature" style="left:481px;top:24px">
    <h3><i><svg width="30" height="30" viewBox="0 0 30 30"><circle cx="11" cy="11" r="6" fill="none" stroke="#fff" stroke-width="4" stroke-dasharray="3 2"/><circle cx="21" cy="21" r="4" fill="none" stroke="#fff" stroke-width="3" stroke-dasharray="2 1.5"/></svg></i>Lorem Ipsum</h3>
    <hr>
    <p>Lorem Ipsum is simply dummy text of the printing and typesetting industry. Lorem Ipsum has been the industry's standard dummy text ever since the Ipsum has been the industry's...</p>
    <div class="btn"><span>Read More</span><b>+</b></div>
  </article>
  <article class="feature" style="left:796px;top:24px;width:288px">
    <h3><i><svg width="30" height="26" viewBox="0 0 30 26"><circle cx="6" cy="4" r="3" fill="#fff"/><circle cx="15" cy="4" r="3" fill="#fff"/><circle cx="24" cy="4" r="3" fill="#fff"/><rect x="3" y="9" width="6" height="15" rx="2" fill="#fff"/><rect x="12" y="9" width="6" height="15" rx="2" fill="#fff"/><rect x="21" y="9" width="6" height="15" rx="2" fill="#fff"/></svg></i>&nbsp;Lorem Ipsum</h3>
    <hr style="margin-left:6px">
    <p style="padding-left:9px">Lorem Ipsum is simply dummy text of the printing and typesetting industry. Lorem Ipsum has been the industry's standard dummy text ever since the Ipsum has been the industry's...</p>
    <div class="btn"><span>Read More</span><b>+</b></div>
  </article>
</section>

<footer class="footer">
  <div class="brand" style="top:46px"><span class="dot"></span>VONTAREX</div>
  <div class="social"><i></i><i></i><i></i></div>
  <nav>
    <a href="#">Home</a><span class="sep">|</span><a href="#">About Us</a><span class="sep">|</span><a href="#">Services</a><span class="sep">|</span><a href="#">Pharmacy</a><span class="sep">|</span><a href="#">Products</a><span class="sep">|</span><a href="#">Contact Us</a><br>
    Vontarex Copyright &nbsp;© 2014, &nbsp;Privacy Policy
  </nav>
</footer>
</body>
</html>
```